Design some Business Cards for Kelvo Systems

I need a design for business cards. I have an existing logo.

I am a sole trader (work for myself) and I provide computer and IT technology support services to small businesses in Australia. I advise business owners on how to best use and manage their IT systems and computers and I provide onsite computer troubleshooting services.
The style should reflect the professional nature of my work.
I would likely favour a simpler and clean design.

The artwork needs to be:
Single sided (just the front of the card)
89mm x 54mm in size.
Full colour.
To be printed on white stock (paper)

Details that need to be included on the business cards are:
Logo
Name Miles BBBBBBBB
Email address miles@kelvosys.example
Phone number 2222 222 222

The exact details will be supplied at the end of the contest for the final artwork.
Final artwork would need to be print ready – I can provide examples of what they need to look like.

```html
<!DOCTYPE html>
<html lang="en">
<head>
<meta charset="utf-8">
<title>Kelvo Systems – Business Card</title>
<link rel="stylesheet" href="https://fonts.googleapis.com/css2?family=Saira+Semi+Condensed:wght@400;500&display=swap">
<style>
  :root {
    --backdrop: #d3e0e4;
    --card: #ffffff;
    --brand-blue: #1f87d2;
    --mark-blue: #2a5fa8;
    --ink-grey: #4d4d4d;
    --tagline-grey: #555555;
  }
  html, body {
    margin: 0;
    padding: 0;
    width: 1194px;
    height: 1200px;
    overflow: hidden;
    background: var(--backdrop);
    font-family: "Saira Semi Condensed", "Arial Narrow", sans-serif;
  }
  .business-card {
    position: absolute;
    left: 185px;
    top: 338px;
    width: 842px;
    height: 527px;
    background: var(--card);
  }
  .brand {
    position: absolute;
    left: 70px;
    top: 68px;
    display: flex;
    align-items: center;
    gap: 30px;
  }
  .brand-mark {
    width: 104px;
    height: 104px;
    display: block;
  }
  .brand-name {
    margin: 0;
    font-size: 70px;
    font-weight: 400;
    line-height: 1;
    color: var(--mark-blue);
    letter-spacing: -0.5px;
  }
  .brand-tagline {
    margin: 4px 0 0 4px;
    font-size: 15px;
    letter-spacing: 1.2px;
    color: var(--tagline-grey);
  }
  .holder {
    position: absolute;
    left: 66px;
    top: 378px;
  }
  .holder-name {
    margin: 0;
    font-size: 37px;
    font-weight: 400;
    line-height: 1.1;
    color: var(--brand-blue);
  }
  .holder-role {
    margin: 6px 0 0;
    font-size: 26px;
    line-height: 1.1;
    color: var(--brand-blue);
  }
  .contact {
    position: absolute;
    right: 74px;
    top: 368px;
    margin: 0;
    padding: 0;
    list-style: none;
    text-align: right;
    font-size: 27px;
    line-height: 42px;
    color: var(--ink-grey);
  }
  .edge-band {
    position: absolute;
    right: 0;
    bottom: 0;
    width: 48px;
    height: 202px;
    background: var(--brand-blue);
  }
</style>
</head>
<body>
  <section class="business-card">
    <header class="brand">
      <svg class="brand-mark" viewBox="0 0 104 104" aria-hidden="true">
        <circle cx="52" cy="52" r="52" fill="#2a5fa8"/>
      </svg>
      <div>
        <h1 class="brand-name">Kelvo Systems</h1>
        <p class="brand-tagline">Computer and IT Problems Solved</p>
      </div>
    </header>

    <div class="holder">
      <h2 class="holder-name">Miles BBBBBBBB</h2>
      <p class="holder-role">Designation</p>
    </div>

    <ul class="contact">
      <li class="contact-email">miles@kelvosys.example</li>
      <li class="contact-phone">2222 222 222</li>
      <li class="contact-web">www.kelvosys.example</li>
    </ul>

    <div class="edge-band"></div>
  </section>
</body>
</html>
```